Velora Crest Label

Design a label for the new brand Velora Crest. The specific product label : Velora Crest Deep Moisturizing Conditioner.

You only need to design the front label.I have included the logo and a bottle jpeg. Please try your best.

Industry/Entity Type

Product

Requirements
Must have
• text you can use:
• For Dry, Damaged Hair
• Strengthening & Moisturizing Conditioner
• Moisture Infused
• Deep Penetrating Formula
• Used by Professionals
• 8.5oz/250ml

```html
<!DOCTYPE html>
<html lang="en">
<head>
<meta charset="utf-8">
<title>Velora Crest Deep Moisturizing Conditioner – Label Options</title>
<link rel="stylesheet" href="https://fonts.googleapis.com/css2?family=Open+Sans:wght@300;400;600&display=swap">
<style>
  :root {
    --backdrop: #cccccc;
    --option-number: #9a9a9a;
    --bottle-red: #8e1a0c;
    --band-green: #c6f04e;
    --band-yellow: #fbe64a;
    --band-gold: #f6d43a;
    --brand-gold: #f2b51e;
    --ink-dark: #1d1d1d;
    --ink-light: #ffffff;
  }
  html, body {
    margin: 0;
    padding: 0;
    width: 1200px;
    height: 900px;
    overflow: hidden;
    background: var(--backdrop);
  }
  .label-sheet {
    display: block;
    width: 1200px;
    height: 900px;
  }
  .option-number {
    font-family: "Open Sans", sans-serif;
    font-weight: 300;
    font-size: 44px;
    fill: var(--option-number);
  }
  .label-body { fill: var(--bottle-red); }
  .brand-name {
    font-family: "Open Sans", sans-serif;
    font-weight: 600;
    fill: var(--brand-gold);
  }
  .product-name {
    font-family: "Open Sans", sans-serif;
    font-weight: 300;
    fill: var(--ink-dark);
  }
  .product-name.on-red { fill: var(--ink-light); }
  .volume {
    font-family: "Open Sans", sans-serif;
    font-weight: 600;
    font-size: 8px;
    fill: var(--ink-dark);
  }
  .volume.on-red { fill: var(--ink-light); font-weight: 400; }
</style>
</head>
<body>
<svg class="label-sheet" viewBox="0 0 1200 900" xmlns="http://www.w3.org/2000/svg">
  <defs>
    <linearGradient id="band-gradient" x1="0" x2="1" y1="0" y2="0">
      <stop offset="0" stop-color="var(--band-green)"/>
      <stop offset="0.45" stop-color="var(--band-gold)"/>
      <stop offset="1" stop-color="var(--band-yellow)"/>
    </linearGradient>
  </defs>

  <!-- Option 1 -->
  <g class="label-option option-one">
    <text class="option-number" x="293" y="60" text-anchor="middle">1</text>
    <path class="label-body" d="M190,800 V300 Q190,213 298,213 Q406,213 406,300 V800 Q298,812 190,800 Z"/>
    <path class="colour-band" fill="url(#band-gradient)"
          d="M190,523 L320,523 C350,523 360,440 406,430 L406,612 Q298,626 190,638 Z"/>
    <text class="brand-name" x="210" y="498" font-size="17">Velora Crest</text>
    <text class="product-name" text-anchor="end" font-size="25">
      <tspan x="390" y="550">DEEP</tspan>
      <tspan x="390" y="580">MOISTURIZING</tspan>
      <tspan x="390" y="611">CONDITIONER</tspan>
    </text>
    <text class="volume" x="388" y="625" text-anchor="end">250 ml.</text>
  </g>

  <!-- Option 2 -->
  <g class="label-option option-two">
    <text class="option-number" x="557" y="60" text-anchor="middle">2</text>
    <path class="label-body" d="M450,800 V300 Q450,213 558,213 Q666,213 666,300 V800 Q558,812 450,800 Z"/>
    <path class="colour-band" fill="url(#band-gradient)"
          d="M450,563 L590,563 C620,563 625,445 666,435 L666,703 Q558,706 450,708 Z"/>
    <text class="brand-name" x="466" y="522" font-size="19">Velora Crest</text>
    <text class="product-name" text-anchor="end" font-size="25">
      <tspan x="648" y="612">DEEP</tspan>
      <tspan x="648" y="643">MOISTURIZING</tspan>
      <tspan x="648" y="674">CONDITIONER</tspan>
    </text>
    <text class="volume" x="648" y="690" text-anchor="end">250 ml.</text>
  </g>

  <!-- Option 3 -->
  <g class="label-option option-three">
    <text class="option-number" x="818" y="60" text-anchor="middle">3</text>
    <path class="label-body" d="M698,800 V300 Q698,213 806,213 Q914,213 914,300 V800 Q806,812 698,800 Z"/>
    <path class="colour-band" fill="url(#band-gradient)"
          d="M698,640 Q770,630 790,618 Q800,612 805,603 Q810,612 820,618 Q840,630 914,632
             L914,647 Q840,647 815,632 Q808,628 805,622 Q802,628 795,632 Q770,650 698,656 Z"/>
    <text class="brand-name" x="803" y="460" font-size="16" text-anchor="middle">Velora Crest</text>
    <text class="product-name on-red" text-anchor="middle">
      <tspan x="805" y="532" font-size="24">DEEP</tspan>
      <tspan x="805" y="555" font-size="18">MOISTURIZING</tspan>
      <tspan x="805" y="584" font-size="26">CONDITIONER</tspan>
    </text>
    <text class="volume on-red" x="894" y="673" text-anchor="end">250 ml.</text>
  </g>
</svg>
</body>
</html>
```